U.S. Popcorn company needs business cards

We are a popcorn company that manufactures popcorn and sells it to grocery stores worldwide. Our theme is "Americana" and our logo is Kettle Mesa Byway which is the most famous highway in the U.S.

We would like the design to be simple and to use both sides. On the back side we would like to see just the logo and website. The front would be normal details

Target Market(s)

Wholesalers, grocers and distributors

Industry/Entity Type

Manufacture

Contact Information for Business Card

Business name: Kettle Mesa Popcorn
Phone: +1 555 014 2286
Email: Dale@kettlemesapopcorn.com
website: www.kettlemesapopcorn.com
Tag Line: "POPped fresh daily"
Name: Dale Whitcombe
Title: Founder/President

Requirements
Must have
• Either this design should be fun or clean and simple. I will let you show me your thougths.
Nice to have
• Anything that ties in the real Kettle Mesa Byway.
• Colors might need to be red, white and blue incorporated.
Should not have
• Not be too busy.

```html
<!DOCTYPE html>
<html lang="en">
<head>
<meta charset="utf-8">
<title>Kettle Mesa Popcorn – Business Cards</title>
<link href="https://fonts.googleapis.com/css2?family=Arimo:ital,wght@0,400;0,700;1,400&family=Questrial&display=swap" rel="stylesheet">
<style>
  :root {
    --navy: #12306a;
    --red: #c8201f;
    --white: #ffffff;
    --paper: #f7f7f5;
    --backdrop: #e4e4e4;
    --rule: #d6d6d6;
  }
  * { margin: 0; padding: 0; box-sizing: border-box; }
  html, body { width: 1200px; height: 576px; overflow: hidden; }
  body { background: var(--backdrop); position: relative; font-family: "Arimo", Arial, sans-serif; }

  .card {
    position: absolute; top: 139px; height: 293px; border-radius: 6px; overflow: hidden;
  }

  /* Back side */
  .card-back { left: 82px; width: 484px; background: var(--navy); }
  .card-back .brand {
    position: absolute; left: 0; right: 0; top: 112px; text-align: center;
    font-family: "Questrial", sans-serif; color: var(--white);
    font-size: 34px; line-height: 1.15; letter-spacing: 0.5px;
  }
  .card-back .web-line {
    position: absolute; left: 0; right: 0; top: 256px;
    display: flex; align-items: center; justify-content: center; gap: 10px;
    color: var(--white); font-family: "Questrial", sans-serif; font-size: 11.5px; font-weight: 700; letter-spacing: 0.3px;
  }
  .card-back .web-line .dash { width: 48px; height: 2px; background: var(--red); }

  /* Front side */
  .card-front { left: 602px; width: 481px; background: var(--paper); }
  .card-front .brand-block {
    position: absolute; left: 30px; top: 88px; width: 160px;
    display: flex; flex-direction: column; align-items: center; gap: 8px;
  }
  .card-front .brand-dot { width: 22px; height: 22px; border-radius: 50%; background: var(--red); }
  .card-front .brand {
    font-family: "Questrial", sans-serif; color: var(--navy); font-size: 22px; line-height: 1.15; text-align: center;
  }
  .card-front .divider {
    position: absolute; left: 211px; top: 61px; width: 1px; height: 144px; background: var(--rule);
  }
  .person { position: absolute; left: 239px; top: 66px; }
  .person .name { color: var(--red); font-weight: 700; font-size: 16.5px; line-height: 1.2; }
  .person .title { color: var(--navy); font-style: italic; font-size: 12px; margin-top: 2px; }

  .contacts { position: absolute; left: 239px; top: 151px; list-style: none; }
  .contacts li {
    display: flex; align-items: center; gap: 10px; height: 17.5px;
    color: var(--navy); font-size: 13px;
  }
  .contacts svg { width: 11px; height: 11px; fill: var(--red); flex: none; }
  .contacts .accent { color: var(--red); }

  .band { position: absolute; left: 0; bottom: 0; width: 481px; height: 40px; }
  .tagline {
    position: absolute; left: 238px; top: 264px;
    color: var(--white); font-family: "Questrial", sans-serif; font-size: 14.5px;
  }
  .tagline b { font-family: "Arimo", sans-serif; font-weight: 700; }
</style>
</head>
<body>

  <section class="card card-back" aria-label="Card back">
    <div class="brand">Kettle Mesa<br>Popcorn</div>
    <div class="web-line"><span class="dash"></span>www.kettlemesapopcorn.com<span class="dash"></span></div>
  </section>

  <section class="card card-front" aria-label="Card front">
    <div class="brand-block">
      <span class="brand-dot"></span>
      <div class="brand">Kettle Mesa<br>Popcorn</div>
    </div>
    <div class="divider"></div>

    <div class="person">
      <div class="name">Dale Whitcombe</div>
      <div class="title">Founder/President</div>
    </div>

    <ul class="contacts">
      <li>
        <svg viewBox="0 0 12 12" aria-hidden="true"><path d="M1 4c0-2 2-3 5-3s5 1 5 3l-2 1-1-1.5H4L3 5 1 4zM2.5 6h7l1 5h-9z"/></svg>
        +1 555 014 2286
      </li>
      <li>
        <svg viewBox="0 0 12 12" aria-hidden="true"><path d="M0 2h12v8H0zM0 2l6 4.5L12 2" stroke="#f7f7f5" stroke-width="1"/></svg>
        Dale@kettlemesapopcorn.com
      </li>
      <li>
        <svg viewBox="0 0 12 12" aria-hidden="true"><circle cx="6" cy="6" r="5.5"/><path d="M0.5 6h11M6 0.5c-3 3-3 8 0 11M6 0.5c3 3 3 8 0 11" stroke="#f7f7f5" stroke-width="0.9" fill="none"/></svg>
        <span>www.<span class="accent">kettlemesapopcorn</span>.com</span>
      </li>
    </ul>

    <svg class="band" viewBox="0 0 481 40" preserveAspectRatio="none" aria-hidden="true">
      <rect x="0" y="17" width="220" height="23" fill="var(--red)"/>
      <polygon points="211,0 481,0 481,40 188,40" fill="var(--navy)"/>
    </svg>
    <div class="tagline">"<b>POP</b>ped fresh daily"</div>
  </section>

</body>
</html>
```